Book Cover Design Project

Need a hip, slightly edgy (even a little bit sexy) cover design for a book about The Millennial Generation.

"Quietfolk 202" is a non-fiction book. The target audience/customer is the younger Baby Boomer and most of Generation X, looking to better understand the largest generation on the planet (Millennials). So, the cover should tease the young, hip, edgy vibe of Millennials...without looking too alienating to someone in their 40's or 50's.

Imagine this as a movie poster for a documentary about Millennials-you want to have a cover that intrigues the audience and reminds them that the topic is something the audience doesn't completely understand, without making them feel like it's too cool.

Much of the target audience was the initial audience for QRB, when it started in the early 80's. They're cooler than you might think, and like to think of themselves that way.

Possible inspiration:

-Retro Dale Ostrum movie posters (with an irreverent, contemporary nod to the original)
-Iconic Magazine covers from the 80's or 90's (Think Copper Lantern)
-Stark, fresh, contemporary imagery/style that feels very Brooklyn/Austin/Silverlake in it's vibe.

The final design should convey that this book is a great resource to crack the code of who millennials are, why they are so different, and how to live with that reality.

Reason: Seeing some great work. Been traveling, so can't make a decision right now.

Industry/Entity Type

Movie

Requirements
Must have
• The Title:
"Quietfolk 202"

Subtitle:
"Understanding and Engaging the largest generation on the planet"

(open to most fonts, etc)
Nice to have
• A crisp, recognizable cover that feels like a movie poster or a magazine.
Should not have
• Predictable, cheesy stock photography.

```html
<!DOCTYPE html>
<html lang="en">
<head>
<meta charset="utf-8">
<title>Quietfolk 202 — Book Cover</title>
<link href="https://fonts.googleapis.com/css2?family=Anton&family=Poppins:wght@700&display=swap" rel="stylesheet">
<style>
  :root {
    --backdrop: #e9e6e1;
    --ink-purple: #2a0f7a;
    --ink-black: #141018;
    --pattern-cream: #eed9b8;
    --pattern-pink: #e07ab0;
    --pattern-magenta: #b01e8e;
    --pattern-green: #2fcf8f;
    --pattern-teal: #4a93a0;
    --numeral-tint: rgba(70, 130, 150, 0.55);
  }
  * { box-sizing: border-box; margin: 0; padding: 0; }
  html, body {
    width: 1200px;
    height: 789px;
    overflow: hidden;
    background: var(--backdrop);
  }
  .stage {
    width: 1200px;
    height: 789px;
    display: flex;
    align-items: center;
    justify-content: center;
  }
  .book-cover {
    position: relative;
    width: 520px;
    height: 730px;
    overflow: hidden;
    box-shadow: 0 6px 24px rgba(0, 0, 0, 0.18);
  }
  .cover-pattern {
    position: absolute;
    inset: 0;
    background:
      radial-gradient(ellipse at 30% 20%, rgba(224, 122, 176, 0.55), transparent 55%),
      radial-gradient(ellipse at 75% 65%, rgba(176, 30, 142, 0.45), transparent 55%),
      linear-gradient(160deg,
        var(--pattern-green) 0%,
        var(--pattern-cream) 40%,
        var(--pattern-pink) 70%,
        var(--pattern-green) 100%);
  }
  .cover-title {
    position: absolute;
    top: 18px;
    left: 0;
    width: 100%;
    text-align: center;
    font-family: "Anton", sans-serif;
    font-size: 120px;
    line-height: 1;
    letter-spacing: -2px;
    color: var(--ink-purple);
    text-transform: uppercase;
    transform: scaleY(1.7);
    transform-origin: top center;
    white-space: nowrap;
  }
  .cover-numeral {
    position: absolute;
    top: 260px;
    left: 0;
    width: 100%;
    text-align: center;
    font-family: "Anton", sans-serif;
    font-size: 250px;
    line-height: 1;
    letter-spacing: 10px;
    color: var(--numeral-tint);
  }
  .cover-subtitle {
    position: absolute;
    left: 0;
    bottom: 0;
    width: 100%;
    padding: 12px 14px;
    background: var(--pattern-cream);
    font-family: "Poppins", sans-serif;
    font-weight: 700;
    font-size: 13px;
    line-height: 1.2;
    color: var(--ink-black);
    white-space: nowrap;
    text-align: center;
  }
</style>
</head>
<body>
  <main class="stage">
    <section class="book-cover">
      <div class="cover-pattern" role="img" aria-label="Geometric pattern of small pink, magenta, green, purple and cream triangles"></div>
      <h1 class="cover-title">Quietfolk</h1>
      <p class="cover-numeral">202</p>
      <p class="cover-subtitle">Understanding and Engaging the largest generation on the planet</p>
    </section>
  </main>
</body>
</html>
```